Film Poster: a short documentary about the father of Arabian Racing Horses

NOTE: PLEASE ONLY USE ATTACHED PICTURE

I'd like to design a film poster for my upcoming short documentary to use as part of the marketing material. The film captures the story of a legendary Arabian racing horse, who later become the most influential stallion producing hunderes of champion horses. The film title is "Sahm: The Swift Crest".

I'd like to receive the .psd file to be able to add any festival/awards logos later on as I apply the film to film festivals.

Industry/Entity Type

Film Production

Requirements
Must have
• I'd love the poster to include both Arabic and English titles and they are:
• English: Sahm: The Swift Crest
• Arabic: سهم: حكاية الفارس الأولى
• I'd also like to poster to include the classical credits at the bottom of the poster that includes the following information:
• In Association with MERIDA SCREEN ACADEMY
• Supported by MSA LUMEN CINEMA GRANT
• Directed by KAREEM BELHOUDI
• Produced by KAREEM BELHOUDI and TOM ASHWELL
• Executive Producer RANIA SELWAQ
• Cinematography GREGOR PALVE
• Sound MAZIN QUDSEEB
• Editing SULTAN FERIDOU and TARIQ ELBOUSHRI
Nice to have
• The colours of the horse's team is maroon and white, and it would be nice if I can have a touch of those two colours in the design maybe as a splash on the side or to lines crossing horizontally.

```html
<!DOCTYPE html>
<html lang="en">
<head>
<meta charset="utf-8">
<title>Sahm: The Swift Crest — Poster</title>
<link href="https://fonts.googleapis.com/css2?family=Anton&family=Alfa+Slab+One&family=Lalezar&family=Cairo:wght@900&family=Montserrat:wght@600;700;800&display=swap" rel="stylesheet">
<style>
  :root {
    --maroon: #7d0000;
    --maroon-deep: #2a0000;
    --night: #050000;
    --white: #ffffff;
    --red: #e8232b;
    --label-red: #c0141c;
  }
  html, body { margin: 0; padding: 0; overflow: hidden; background: var(--night); }
  .poster {
    position: relative;
    width: 851px; height: 1200px; overflow: hidden;
    background: linear-gradient(100deg, var(--maroon) 0%, #4a0000 30%, var(--maroon-deep) 52%, var(--night) 72%);
    font-family: "Montserrat", sans-serif;
  }
  .poster__lines { position: absolute; inset: 0; }
  .poster__photo {
    position: absolute; left: 330px; top: 370px; width: 560px; height: 860px;
    background: radial-gradient(ellipse 45% 55% at 55% 45%, #e8e6e1 0%, #cfcbc4 45%, #8e8a85 70%, rgba(20,10,10,0) 100%);
  }
  .title-en {
    position: absolute; left: 178px; top: 84px; margin: 0;
    font-family: "Anton", sans-serif; font-size: 118px; line-height: 1;
    color: var(--white); letter-spacing: 1px;
  }
  .subtitle-en {
    position: absolute; left: 180px; top: 184px; margin: 0;
    font-family: "Alfa Slab One", serif; font-size: 23px; line-height: 1;
    color: var(--red); letter-spacing: 1px;
  }
  .title-ar {
    position: absolute; right: 115px; top: 150px; margin: 0;
    font-family: "Lalezar", sans-serif; font-size: 300px; line-height: 0.9;
    color: var(--white); direction: rtl;
  }
  .subtitle-ar {
    position: absolute; right: 115px; top: 372px; margin: 0;
    font-family: "Cairo", sans-serif; font-weight: 900; font-size: 54px; line-height: 1.3;
    color: var(--red); direction: rtl;
  }
  .credit { position: absolute; }
  .credit__label { display: block; color: var(--label-red); font-size: 10.5px; font-weight: 600; line-height: 1.2; }
  .credit__name { display: block; color: var(--white); font-size: 12.5px; font-weight: 700; line-height: 1.15; }
  .credit__name--small { font-size: 10px; }
  .partner { display: block; color: var(--white); font-size: 9px; font-weight: 800; line-height: 1.2; margin-top: 6px; width: 110px; }
</style>
</head>
<body>
<main class="poster">
  <div class="poster__photo" role="img" aria-label="Portrait of a white Arabian stallion in a leather halter against a dark stable"></div>

  <svg class="poster__lines" width="851" height="1200" viewBox="0 0 851 1200" aria-hidden="true">
    <line x1="255" y1="82" x2="790" y2="52" stroke="#b3121a" stroke-width="1.5"/>
    <line x1="50" y1="486" x2="851" y2="440" stroke="#b3121a" stroke-width="1.5"/>
  </svg>

  <h1 class="title-en">SAHM</h1>
  <p class="subtitle-en">THE SWIFT CREST</p>
  <p class="title-ar" lang="ar">سهم</p>
  <p class="subtitle-ar" lang="ar">حكاية الفارس الأولى</p>

  <div class="credit" style="left:89px; top:1008px;">
    <span class="credit__label">In Association with</span>
    <span class="partner">MERIDA SCREEN ACADEMY</span>
  </div>
  <div class="credit" style="left:89px; top:1092px;">
    <span class="credit__label">Supported by</span>
    <span class="partner">MSA LUMEN CINEMA GRANT</span>
  </div>

  <div class="credit" style="left:211px; top:1092px;">
    <span class="credit__label">Directed by</span>
    <span class="credit__name">KAREEM BELHOUDI</span>
  </div>
  <div class="credit" style="left:211px; top:1138px;">
    <span class="credit__label">Sound</span>
    <span class="credit__name">MAZIN QUDSEEB</span>
  </div>

  <div class="credit" style="left:380px; top:1092px;">
    <span class="credit__label">Produced by</span>
    <span class="credit__name">KAREEM BELHOUDI</span>
    <span class="credit__name">TOM ASHWELL</span>
  </div>
  <div class="credit" style="left:378px; top:1140px;">
    <span class="credit__label">Editing</span>
    <span class="credit__name credit__name--small">SULTAN FERIDOU</span>
    <span class="credit__name credit__name--small">TARIQ ELBOUSHRI</span>
  </div>

  <div class="credit" style="left:570px; top:1092px;">
    <span class="credit__label">Executive Producer</span>
    <span class="credit__name">RANIA SELWAQ</span>
  </div>
  <div class="credit" style="left:570px; top:1138px;">
    <span class="credit__label">Cinematography</span>
    <span class="credit__name">GREGOR PALVE</span>
  </div>
</main>
</body>
</html>
```